Pro-life non-profit needs a dynamic poster design for their Christmas Gala.

We need a poster design which plays off the name of the event, The Winter Lantern. The Winter Lantern, of course is the Baby Jesus. Our cause supports unborn children in Iowa. The gala will include a concert of popular Christmas music sung by top soloists backed by an orchestra. An original commissioned song, The Winter Lantern, will be premiered. Purple and gold colors immediately come to mind, but a designer should not feel constrained on colors. We need an editable design w/fonts. Photoshop w/layers or Illustrator files are good.

```html
<!DOCTYPE html>
<html lang="en">
<head>
<meta charset="utf-8">
<title>The Winter Lantern – Christmas Gala Poster</title>
<link rel="stylesheet" href="https://fonts.googleapis.com/css2?family=Playfair+Display:ital,wght@0,500;0,600;1,500&family=Lato:wght@400;700&display=swap">
<style>
  :root {
    --paper: #ffffff;
    --purple: #5e4a77;
    --gold: #d2ad62;
    --gold-soft: #e6cd93;
    --ink-light: #f6f1fa;
    --cream: #f3e6cf;
    --swaddle: #efe2d0;
    --swaddle-shade: #dcc6a8;
  }
  * { margin: 0; padding: 0; box-sizing: border-box; }
  html, body { width: 849px; height: 1200px; overflow: hidden; background: var(--paper); }
  .poster {
    position: relative;
    width: 849px;
    height: 1200px;
    background: var(--paper);
    font-family: "Lato", Arial, sans-serif;
    color: var(--ink-light);
    overflow: hidden;
  }
  .panel {
    position: absolute;
    left: 40px; top: 22px;
    width: 780px; height: 1140px;
    background: var(--purple);
    border: 4px solid var(--gold);
    overflow: hidden;
  }
  .nativity-art {
    position: absolute;
    right: 0; bottom: 0;
    width: 330px; height: 245px;
    background:
      radial-gradient(ellipse 70% 75% at 70% 70%, var(--swaddle) 0%, var(--swaddle-shade) 55%, rgba(220,198,168,0) 100%);
  }
  .panel-frame {
    position: absolute;
    left: 52px; top: 34px;
    width: 756px; height: 1116px;
    border: 1.5px solid var(--gold-soft);
  }
  .corner-sprig {
    position: absolute;
    top: 40px;
    width: 120px; height: 70px;
    background: radial-gradient(ellipse at center, rgba(230,205,147,0.3), rgba(230,205,147,0) 70%);
  }
  .corner-sprig.left { left: 60px; }
  .corner-sprig.right { right: 60px; }
  .copy {
    position: absolute;
    left: 180px; width: 530px;
    text-align: center;
  }
  .org { top: 38px; font-size: 22px; }
  .presents { top: 66px; font-family: "Playfair Display", Georgia, serif; font-style: italic; font-size: 18px; }
  .banquet { top: 90px; font-size: 21px; }
  .rule {
    position: absolute;
    left: 200px; width: 490px; height: 0;
    border-top: 2px solid var(--gold);
  }
  .title {
    top: 138px;
    font-family: "Playfair Display", Georgia, serif;
    font-weight: 500;
    font-size: 56px;
    color: var(--cream);
  }
  .subtitle {
    top: 215px;
    font-family: "Playfair Display", Georgia, serif;
    font-size: 26px;
    letter-spacing: 1px;
  }
  .date { top: 284px; font-family: "Playfair Display", Georgia, serif; font-size: 30px; }
  .date em { font-style: italic; font-size: 36px; }
  .doors { top: 338px; font-family: "Playfair Display", Georgia, serif; font-size: 24px; }
  .venue { top: 384px; font-weight: 700; font-size: 18px; }
  .price { top: 443px; font-family: "Playfair Display", Georgia, serif; font-size: 24px; }
  .program { top: 508px; font-family: "Playfair Display", Georgia, serif; font-size: 25px; }
  .speaker-label { top: 586px; font-size: 22px; font-weight: 700; color: var(--gold-soft); }
  .speaker { top: 625px; font-size: 30px; font-weight: 700; }
  .seating { top: 730px; font-size: 16px; font-weight: 700; color: var(--gold-soft); line-height: 24px; letter-spacing: 0.5px; }
  .order { top: 826px; font-size: 16px; line-height: 26px; }
  .order strong { font-weight: 700; }
</style>
</head>
<body>
<main class="poster">
  <div class="panel">
    <div class="nativity-art" role="img" aria-label="Illustration of the infant in the manger wrapped in white cloth with a golden halo"></div>
  </div>
  <div class="panel-frame"></div>
  <div class="corner-sprig left" role="img" aria-label="Gold winter sprig ornament"></div>
  <div class="corner-sprig right" role="img" aria-label="Gold winter sprig ornament"></div>

  <p class="copy org">Heartland Voices for Life</p>
  <p class="copy presents">presents</p>
  <p class="copy banquet">The Tenth Annual Fundraising Banquet</p>
  <div class="rule" style="top:118px"></div>

  <h1 class="copy title">The Winter Lantern</h1>
  <p class="copy subtitle">A PRO-LIFE, CHRISTMAS GALA</p>
  <div class="rule" style="top:263px"></div>

  <p class="copy date"><em>Saturday,</em> November 21st 2020</p>
  <p class="copy doors">Doors open at 5:30 PM</p>
  <p class="copy venue">Maple Grove Hall, Riverton, IA</p>
  <div class="rule" style="top:425px"></div>

  <p class="copy price">$60 person • $500 table of ten</p>
  <div class="rule" style="top:489px"></div>

  <p class="copy program">Cocktails • Dinner • Christmas Concert</p>
  <div class="rule" style="top:560px"></div>

  <p class="copy speaker-label">Special Guest Speaker</p>
  <p class="copy speaker">Bishop Thomas Aldren</p>
  <div class="rule" style="top:690px"></div>

  <p class="copy seating">SEATING LIMITED<br>RESERVATIONS NEEDED</p>
  <div class="rule" style="top:800px"></div>

  <p class="copy order"><strong>Order tickets online : www.HeartlandVoices.org</strong><br>515-555-0142 &nbsp; events@heartlandvoices.org</p>
</main>
</body>
</html>
```